I would like a flyer for the ultimate masquarade ball. This will be a PARTY! We need a flyer that will jump out and catch the attention of anyone who sees it. We would like plenty of purple and gold to be used in the flyer. The final design should communicate the ultmate, upscale, classy, exciting masquarade ball ever!

This flyer must be designed for high resolution for printing on 4" x 6" flyers.

Industry/Entity Type

Printing

Requirements
Must have
• Rho Kappa Chapter Presents
Sigma Violet & Amber MasQUErade Gala
1 March 2014
8pm - 1am
3-Course Plated Dinner
Cash Bar
RSVP By: 28 Feb 2014
Halvorsen Gaming & Downs, Larkspur Banquet Hall
DJ Tarvek
Details & Tickets: http://sigmavioletambergala.ticketlark.example
More Info? 555-317-8826
Dress Code: Black Tie & Traditional Dress, Costumes & Masks Preferred

```html
<!DOCTYPE html>
<html lang="en">
<head>
<meta charset="utf-8">
<title>Sigma Violet &amp; Amber Masquerade Gala</title>
<link href="https://fonts.googleapis.com/css2?family=Cinzel:wght@400;500&family=Great+Vibes&display=swap" rel="stylesheet">
<style>
  :root {
    --page: #ffffff;
    --night: #08020f;
    --violet: #4a1a63;
    --violet-deep: #2a0c36;
    --amber: #b98a3a;
    --amber-light: #d9b56a;
    --cream: #f3dcb6;
    --rose-beige: #c7a597;
    --bronze: #6e5434;
  }
  * { margin: 0; padding: 0; box-sizing: border-box; }
  html, body { width: 1200px; height: 987px; overflow: hidden; background: var(--page); }
  .flyer {
    position: absolute; left: 60px; top: 128px; width: 1120px; height: 757px;
    background: var(--night); overflow: hidden;
    font-family: "Cinzel", "Times New Roman", serif; color: var(--cream);
  }
  .flyer__sweep { position: absolute; inset: 0; }
  .text { position: absolute; text-align: center; white-space: nowrap; }
  .presenter { left: 0; width: 1120px; top: 50px; font-size: 30px; font-weight: 500; letter-spacing: 1px; }
  .presents { left: 0; width: 1120px; top: 90px; font-size: 20px; letter-spacing: 1.5px; }
  .info { font-size: 19px; line-height: 31px; letter-spacing: 0.5px; }
  .info--left { left: 52px; width: 300px; top: 144px; }
  .info--right { left: 730px; width: 360px; top: 142px; }
  .info__dj { font-size: 21px; }
  .mask-art {
    position: absolute; left: 418px; top: 137px; width: 280px; height: 208px;
    background: radial-gradient(ellipse 50% 40% at 50% 38%, #3a2a1c 0%, #1e150d 55%, rgba(30,21,13,0.4) 75%, rgba(8,2,15,0) 100%);
    border-radius: 45% 45% 40% 40%;
  }
  .rule { position: absolute; left: 205px; width: 710px; height: 4px;
    background: linear-gradient(90deg, var(--bronze), var(--amber-light) 50%, var(--amber)); }
  .rule--top { top: 345px; }
  .rule--bottom { top: 523px; }
  .gala-title { left: 0; width: 1120px; top: 362px; color: var(--rose-beige); }
  .gala-title__line1 { font-size: 37px; letter-spacing: 1.5px; }
  .gala-title__amp { font-family: "Great Vibes", cursive; font-size: 64px; vertical-align: -2px; }
  .gala-title__line2 { display: block; font-family: "Great Vibes", cursive; font-size: 66px; line-height: 60px; margin-top: -6px; }
  .date { left: 0; width: 1120px; top: 490px; font-size: 21px; letter-spacing: 1px; }
  .tickets-label { left: 0; width: 1120px; top: 571px; font-size: 19px; font-weight: 500; letter-spacing: 1px; }
  .tickets-link {
    position: absolute; left: 298px; top: 606px; width: 524px; height: 33px;
    border: 1px solid var(--cream); font-size: 16px; letter-spacing: 0.6px;
    display: flex; align-items: center; justify-content: center; white-space: nowrap; font-weight: 500;
  }
  .more-info { left: 0; width: 1120px; top: 653px; font-size: 19px; letter-spacing: 1px; font-weight: 500; }
  .dress-band {
    position: absolute; left: 0; top: 695px; width: 1120px; height: 62px;
    background: var(--violet-deep); display: flex; align-items: center; justify-content: center;
    font-size: 19px; letter-spacing: 0.8px; font-weight: 500;
  }
</style>
</head>
<body>
<main class="flyer">
  <svg class="flyer__sweep" width="1120" height="757" viewBox="0 0 1120 757" aria-hidden="true">
    <defs>
      <filter id="soften" x="-20%" y="-50%" width="140%" height="200%"><feGaussianBlur stdDeviation="14"/></filter>
      <linearGradient id="amberFade" x1="0" x2="1"><stop offset="0" stop-color="#7a6030"/><stop offset="0.5" stop-color="#c69a45"/><stop offset="1" stop-color="#5a4424"/></linearGradient>
      <linearGradient id="violetFade" x1="0" x2="1"><stop offset="0" stop-color="#3a1450"/><stop offset="0.6" stop-color="#5b2378"/><stop offset="1" stop-color="#2b0f3a"/></linearGradient>
    </defs>
    <polygon points="0,60 1110,190 1110,570 0,690" fill="#1a0a22"/>
    <g filter="url(#soften)">
      <polygon points="0,95 1110,200 1110,225 0,125" fill="#8a7658" opacity="0.7"/>
      <polygon points="0,150 1110,240 1110,300 0,215" fill="url(#amberFade)" opacity="0.55"/>
      <polygon points="0,240 1110,300 1110,380 0,330" fill="url(#violetFade)" opacity="0.9"/>
      <polygon points="0,360 1110,400 1110,440 0,410" fill="url(#amberFade)" opacity="0.45"/>
      <polygon points="0,430 1110,450 1110,520 0,500" fill="url(#violetFade)" opacity="0.8"/>
      <polygon points="0,520 1110,510 1110,560 0,600" fill="url(#amberFade)" opacity="0.55"/>
    </g>
  </svg>

  <div class="text presenter">Rho Kappa Chapter</div>
  <div class="text presents">Presents</div>

  <div class="text info info--left">
    <div>3-Course Plated Dinner</div>
    <div>Cash Bar</div>
    <div>RSVP By: 28 Feb 2014</div>
  </div>

  <div class="mask-art" role="img" aria-label="Ornate black and gold masquerade mask with a soft reflection"></div>

  <div class="text info info--right">
    <div class="info__dj">- DJ Tarvek -</div>
    <div>Halvorsen Gaming &amp; Downs</div>
    <div>Larkspur Banquet Hall</div>
  </div>

  <div class="rule rule--top"></div>
  <h1 class="text gala-title">
    <span class="gala-title__line1">Sigma Violet <span class="gala-title__amp">&amp;</span></span>
    <span class="gala-title__line2">Amber Masquerade Gala</span>
  </h1>
  <div class="text date">1 March 2014 &nbsp;I&nbsp; 8pm - 1am</div>
  <div class="rule rule--bottom"></div>

  <div class="text tickets-label">Details &amp; Tickets:</div>
  <div class="tickets-link">http://sigmavioletambergala.ticketlark.example</div>
  <div class="text more-info">More Info : 555-317-8826</div>

  <div class="dress-band">Dress Code: Black Tie &amp; Traditional Dress, Costumes &amp; Masks Preferred</div>
</main>
</body>
</html>
```